Business cards and stationary design

We just completed the design of our new logo and we need to print new business cards and letterhead for our nonprofit. We are looking for a fresh new design that shows off our new logo. On letterhead, we must have a column on the right or left to include our Board of Directors (up to 45 names) (see attachment)

Industry/Entity Type

Non-Profit

Contact Information for Business Card

Standard business card with name, title, Company name, mailing address phone numbers, email address and website. Tagline on back "Opening every door to home"

Font styles to use
Sans Serif

Requirements
Must have
• include pertinent information above
• new logo
• fonts compatible with logo
• should use logo colors only
Nice to have
• tag lines

```html
<!DOCTYPE html>
<html lang="en">
<head>
<meta charset="utf-8">
<title>Hearthway Shelter Network – Business Card</title>
<link href="https://fonts.googleapis.com/css2?family=Lato:wght@400;700&display=swap" rel="stylesheet">
<style>
  :root{
    --backdrop:#4a7f5c;
    --card:#ffffff;
    --teal:#0681a0;
    --red:#e8202a;
    --gold:#f6b332;
    --ink:#4b4b4b;
  }
  *{margin:0;padding:0;box-sizing:border-box}
  html,body{width:1200px;height:1200px;overflow:hidden}
  body{background:var(--backdrop);font-family:"Lato",sans-serif;position:relative}
  .card{position:absolute;left:180px;width:840px;height:480px;background:var(--card)}
  .card-front{top:84px}
  .card-back{top:636px}

  .brand{display:flex;align-items:center;gap:12px;color:var(--teal);font-weight:700;font-family:"Lato",sans-serif;white-space:nowrap}
  .brand-mark{width:28px;height:28px;background:var(--teal);flex:none}

  .card-front .brand{position:absolute;left:128px;top:150px;font-size:30px;letter-spacing:.5px;line-height:1}
  .tagline{position:absolute;left:256px;width:328px;text-align:right;top:226px;font-size:24px;line-height:1.1;color:var(--teal);white-space:nowrap}

  .card-back .brand{position:absolute;left:64px;top:122px;font-size:24px;letter-spacing:.3px;line-height:1}
  .card-back .brand-mark{width:24px;height:24px}

  .person{position:absolute;right:30px;top:204px;text-align:right;color:var(--ink)}
  .person-name{font-size:29px;line-height:1.1}
  .person-title{font-size:16px;line-height:1.2;margin-top:2px}
  .divider{position:absolute;left:26px;right:30px;top:261px;height:2px;background:var(--teal)}

  .contacts{position:absolute;left:30px;top:296px;list-style:none;color:var(--ink);font-size:19px}
  .contacts li{display:flex;align-items:center;height:34.5px;white-space:nowrap}
  .contacts svg{width:26px;height:22px;margin-right:14px;flex:none}

  .address-band{position:absolute;left:0;right:0;top:431px;height:49px;background:var(--teal);color:#fff;font-size:19px;display:flex;align-items:center;justify-content:flex-end;padding-right:30px;gap:14px;white-space:nowrap}
  .address-band svg{width:22px;height:28px;flex:none}
</style>
</head>
<body>
  <section class="card card-front">
    <div class="brand"><span class="brand-mark"></span>Hearthway Shelter Network</div>
    <p class="tagline">“Opening every door to home”</p>
  </section>

  <section class="card card-back">
    <div class="brand"><span class="brand-mark"></span>Hearthway Shelter Network</div>

    <div class="person">
      <p class="person-name">Marcus Delane</p>
      <p class="person-title">Board Of Directors</p>
    </div>
    <div class="divider"></div>

    <ul class="contacts">
      <li>
        <svg viewBox="0 0 26 22" aria-hidden="true"><path d="M1 7c0-3 5-5 12-5s12 2 12 5v2h-6V6H7v3H1z" fill="#4b4b4b"/><rect x="4" y="10" width="18" height="10" rx="2" fill="#4b4b4b"/><circle cx="13" cy="15" r="3" fill="#fff"/></svg>
        555-014-2276
      </li>
      <li>
        <svg viewBox="0 0 26 22" aria-hidden="true"><rect x="1" y="4" width="24" height="15" fill="#4b4b4b"/><path d="M1 4l12 9 12-9M1 19l9-7M25 19l-9-7" stroke="#fff" stroke-width="1.5" fill="none"/></svg>
        @hearthwayshelter.org
      </li>
      <li>
        <svg viewBox="0 0 26 22" aria-hidden="true"><g fill="none" stroke="#4b4b4b" stroke-width="1.4"><circle cx="13" cy="11" r="10"/><ellipse cx="13" cy="11" rx="4.5" ry="10"/><path d="M3 11h20M5 5.5h16M5 16.5h16M13 1v20"/></g></svg>
        www.hearthwayshelter.org
      </li>
    </ul>

    <div class="address-band">
      <svg viewBox="0 0 22 28" aria-hidden="true"><path d="M11 26C5 18 2 13.5 2 10a9 9 0 0 1 18 0c0 3.5-3 8-9 16z" fill="none" stroke="#fff" stroke-width="1.5"/><circle cx="11" cy="10" r="3.2" fill="none" stroke="#fff" stroke-width="1.5"/></svg>
      <span>P.O Box 208815, Rivermont, Texas 75390 • 214.555.0187</span>
    </div>
  </section>
</body>
</html>
```